Harborvale Ventures brochure for Investment partnership, young harold pembly

We need a brochure design to attract new investors for our investing partnership Called Harborvale Ventures. We are based in New Orleans, La. We primarily invest in stocks, bonds, and crypto but venture out into other categories as well. We would like to see designs with the black and gold like our logo. The final design should say new, fresh, sleek, tech, and honorable. BROUCHURE WILL BE 4 pages.or one folded sheet a paparer if that makes sense.
Updates

A chart showing Harborvale Ventures gains since 2019 28.6 percent and the TR 400 gAINS 7.1 PERCENT

Target Market(s)

Probable Investors

Industry/Entity Type

Financial Planning

Colors

Designer to choose only greyscale colors for use in the design.

Requirements
Must have
• Black and Gold accent. Stock market feel. Sleek, High tech, innovative, Intellgent design.
Nice to have
• Page colors possibly black.
Should not have
• Boring, Old school,

```html
<!DOCTYPE html>
<html lang="en">
<head>
<meta charset="utf-8">
<title>Harborvale Ventures Brochure</title>
<link href="https://fonts.googleapis.com/css2?family=Cinzel:wght@400;600&family=Tinos&family=Source+Sans+3:wght@400;700&display=swap" rel="stylesheet">
<style>
:root{
  --backdrop:#d3d4d6;
  --ink:#111;
  --night:#151515;
  --charcoal:#2c2c2c;
  --gold:#e9c13c;
  --gold-soft:#f3d46a;
  --gold-deep:#c9961f;
  --paper:#fff;
  --mist:#ddd;
}
*{margin:0;padding:0;box-sizing:border-box}
html,body{width:961px;height:1200px;overflow:hidden;background:var(--backdrop)}
body{position:relative;font-family:"Source Sans 3",sans-serif;color:var(--ink)}
.spread{position:absolute;left:97px;width:794px;height:514px;box-shadow:0 8px 8px -4px rgba(0,0,0,.35);overflow:hidden;background:var(--paper)}
.spread--outer{top:54px}
.spread--inner{top:616px}
.spread svg.art{position:absolute;left:0;top:0;width:794px;height:514px}
.t{position:absolute;white-space:nowrap}
.center{transform:translateX(-50%);text-align:center}
.brand{font-family:"Cinzel",serif;font-weight:600;text-align:center;line-height:1.05}
.brand--dark{color:var(--ink);font-size:25px;left:199px;top:190px}
.brand--gold{color:var(--gold);font-size:27px;left:596px;top:34px}
.brand-rule{position:absolute;height:1px}
.tagline{font-family:"Tinos",serif;color:var(--gold);font-size:12.5px;line-height:17px;left:199px;top:260px}
.intro{font-size:9.4px;line-height:14.5px;left:199px;top:310px}
.contact{left:27px;top:442px;color:#fff}
.contact h3{font-weight:400;font-size:11px;margin-bottom:4px}
.contact p{font-size:9px;line-height:15.5px;display:flex;align-items:center;gap:5px}
.contact svg{width:11px;height:11px}
.cta-text{font-family:"Cinzel",serif;color:var(--mist);font-size:11.3px;letter-spacing:.6px;line-height:13px;left:596px;top:432px}
.web-btn{position:absolute;left:513px;width:164px;height:20px;font-size:10.3px;display:flex;align-items:center;justify-content:center}
.web-btn--gold{top:483px;border:1px solid var(--gold);color:var(--gold)}
.web-btn--dark{top:474px;border:1px solid var(--ink);color:var(--ink)}
.about-title{font-family:"Tinos",serif;color:var(--gold);font-size:13.5px;line-height:17px;left:17px;top:326px}
.about-rule{position:absolute;left:17px;top:371px;width:63px;height:1px;background:var(--gold)}
.about-body{left:17px;top:385px;color:#fff;font-size:9.4px;line-height:14.6px}
.how-title{font-family:"Tinos",serif;font-size:12.5px;letter-spacing:.5px;left:594px;top:32px}
.how-rule{position:absolute;left:511px;top:62px;width:171px;height:1px;background:var(--gold)}
.step-icon{position:absolute;left:443px;width:37px;height:36px;border:1px solid var(--gold);box-shadow:0 1px 2px rgba(0,0,0,.25);background:#fff;display:flex;align-items:center;justify-content:center}
.step-icon svg{width:20px;height:20px}
.step{left:494px;font-size:9.4px;line-height:14.6px}
.step b{font-weight:700}
.step-sep{position:absolute;left:443px;width:325px;border-top:1px dotted #bbb}
</style>
</head>
<body>

<section class="spread spread--outer">
  <svg class="art" viewBox="0 0 794 514" aria-hidden="true">
    <defs>
      <linearGradient id="goldA" x1="0" y1="0" x2="1" y2="1"><stop offset="0" stop-color="#f7d85a"/><stop offset=".6" stop-color="#e3b23a"/><stop offset="1" stop-color="#b9861c"/></linearGradient>
      <linearGradient id="darkA" x1="0" y1="0" x2="1" y2="0"><stop offset="0" stop-color="#1b1b1b"/><stop offset=".6" stop-color="#3a3a3a"/><stop offset="1" stop-color="#1e1e1e"/></linearGradient>
      <linearGradient id="darkB" x1="0" y1="0" x2="1" y2="1"><stop offset="0" stop-color="#111"/><stop offset="1" stop-color="#2f2f2f"/></linearGradient>
      <linearGradient id="paperFade" x1="0" y1="0" x2="1" y2="0"><stop offset=".7" stop-color="#fff"/><stop offset="1" stop-color="#d9d9d9"/></linearGradient>
    </defs>
    <rect x="0" y="0" width="397" height="514" fill="url(#paperFade)"/>
    <rect x="397" y="0" width="397" height="514" fill="url(#darkB)"/>
    <polygon role="img" aria-label="Faded photo of old city balconies and rooftops" points="0,0 397,0 397,143 0,100" fill="#555"/>
    <polygon points="0,387 397,507 397,514 0,514" fill="url(#darkA)"/>
    <polygon points="397,369 257,465 397,507" fill="url(#goldA)"/>
    <rect x="0" y="0" width="397" height="100" fill="url(#darkA)" opacity=".0"/>
    <rect x="442" y="3" width="310" height="105" fill="#0b0b0b"/>
    <polygon role="img" aria-label="Black and white photo of a streetcar on a palm-lined avenue" points="397,143 794,100 794,319 490,413 397,369" fill="#8d8d8d"/>
    <polygon points="397,369 490,413 397,445" fill="url(#goldA)"/>
    <line x1="397" y1="0" x2="397" y2="514" stroke="#999" stroke-width=".6"/>
  </svg>

  <div class="t brand brand--dark center">HARBORVALE<br><span style="font-size:13px;letter-spacing:4px">VENTURES</span></div>
  <div class="brand-rule" style="left:142px;top:218px;width:115px;background:var(--ink)"></div>

  <p class="t tagline center">If you are receiving this brochure its because someone sees you<br>as a person that doesn’t want to just work and pay bills.</p>
  <div class="brand-rule" style="left:64px;top:303px;width:280px;background:var(--gold)"></div>
  <p class="t intro center">Your someone who wants to build real generational wealth.<br>Not throw schemes but the using the greatest wealth builder available.<br>The stock market.</p>

  <div class="t contact">
    <h3>CONTACT US</h3>
    <p><svg viewBox="0 0 12 12"><circle cx="6" cy="6" r="6" fill="#e9c13c"/><path d="M4 3l1.2 1.4-.6.9c.5 1 1.1 1.6 2.1 2.1l.9-.6L9 8c-.3.8-1 1.2-1.8.9C5.4 8.3 3.7 6.6 3.1 4.8 2.8 4 3.2 3.3 4 3z" fill="#222"/></svg>0198 765 432</p>
    <p><svg viewBox="0 0 12 12"><circle cx="6" cy="6" r="6" fill="#e9c13c"/><circle cx="6" cy="6" r="3.6" fill="none" stroke="#222" stroke-width=".8"/><path d="M2.4 6h7.2M6 2.4c-1.6 2-1.6 5.2 0 7.2M6 2.4c1.6 2 1.6 5.2 0 7.2" stroke="#222" stroke-width=".7" fill="none"/></svg>www.HARBORVALEVENTURES.com</p>
    <p><svg viewBox="0 0 12 12"><circle cx="6" cy="6" r="6" fill="#e9c13c"/><path d="M6 2.5a2.3 2.3 0 0 1 2.3 2.3C8.3 6.6 6 9.3 6 9.3S3.7 6.6 3.7 4.8A2.3 2.3 0 0 1 6 2.5z" fill="#222"/><circle cx="6" cy="4.8" r=".9" fill="#e9c13c"/></svg>48 Lantern Row</p>
  </div>

  <div class="t brand brand--gold center">HARBORVALE<br><span style="font-size:17px;letter-spacing:6px">VENTURES</span></div>
  <div class="brand-rule" style="left:523px;top:65px;width:146px;background:var(--gold)"></div>

  <p class="t cta-text center">BECOME A PARTNER AND BUILD GENERATIONAL<br>WEALTH BY INVESTING IN THE STOCK MARKET<br>A FIRST OF ITS KIND INVESTMENT CLUB</p>
  <div class="web-btn web-btn--gold">www.HARBORVALEVENTURES.com</div>
</section>

<section class="spread spread--inner">
  <svg class="art" viewBox="0 0 794 514" aria-hidden="true">
    <defs>
      <linearGradient id="goldB" x1="0" y1="0" x2="1" y2="1"><stop offset="0" stop-color="#f8e06a"/><stop offset=".5" stop-color="#e9bd38"/><stop offset="1" stop-color="#c48f1d"/></linearGradient>
      <linearGradient id="darkC" x1="0" y1="0" x2="1" y2="1"><stop offset="0" stop-color="#2a2a2a"/><stop offset=".5" stop-color="#3b3b3b"/><stop offset="1" stop-color="#121212"/></linearGradient>
      <linearGradient id="paperFade2" x1="0" y1="0" x2="1" y2="0"><stop offset=".75" stop-color="#fff"/><stop offset="1" stop-color="#cfcfcf"/></linearGradient>
    </defs>
    <rect x="0" y="0" width="397" height="514" fill="url(#darkC)"/>
    <rect x="397" y="0" width="397" height="514" fill="url(#paperFade2)"/>
    <polygon points="0,178 281,293 425,0 419,0 276,296 0,184" fill="url(#goldB)"/>
    <polygon role="img" aria-label="Black and white photo of a cathedral and a narrow balconied lane" points="0,0 416,0 276,296 0,182" fill="#7a7a7a"/>
    <polygon points="397,346 794,514 397,514" fill="url(#goldB)"/>
    <polygon points="678,462 794,410 794,514" fill="#1c1c1c"/>
  </svg>

  <p class="t about-title">ABOUT HARBORVALE VENTURES<br>AND GENERAL PARTNER</p>
  <div class="about-rule"></div>
  <p class="t about-body">Harborvale Ventures was founded in 2019 by General Partner Marcus Delaney Jr with<br>a group economic empowerment mission. Marcus Delaney has invested int stocks<br>since a teenager received his BA in ecomics from Bayou State<br>University and is currently attending Gulf Coast University.</p>

  <h2 class="t how-title center" style="font-weight:400">HOW IT WORKS</h2>
  <div class="how-rule"></div>

  <div class="step-icon" style="top:98px"><svg viewBox="0 0 20 20"><rect x="3" y="5" width="14" height="10" rx="2" fill="none" stroke="#111" stroke-width="1.6"/><rect x="3" y="8" width="14" height="2" fill="#111"/></svg></div>
  <p class="t step" style="top:96px"><b>MAKE INITIAL DEPOSIT</b><br>The general partner will invest in stocks, bonds<br>and other investment vehicles on your behalf.</p>
  <div class="step-sep" style="top:149px"></div>

  <div class="step-icon" style="top:170px"><svg viewBox="0 0 20 20"><rect x="2" y="6" width="16" height="9" fill="none" stroke="#111" stroke-width="1.4"/><rect x="4" y="4" width="14" height="1.2" fill="#111"/><circle cx="10" cy="10.5" r="2.2" fill="none" stroke="#111" stroke-width="1.2"/></svg></div>
  <p class="t step" style="top:167px"><b>THERE IS NO UPFRONT FEES</b><br>The general partner will guarantee a 5 percent return<br>and will work for free on your behalf until that is achieved.<br>After the 5 percent return on the dollars invested the limited<br>partner will receive 80 percent and the general partner<br>will receive 20 percent of every dollar gained</p>
  <div class="step-sep" style="top:269px"></div>

  <div class="step-icon" style="top:285px"><svg viewBox="0 0 20 20"><rect x="3" y="14" width="2" height="2" fill="#111"/><rect x="6.5" y="12" width="2" height="4" fill="#111"/><rect x="10" y="9" width="2" height="7" fill="#111"/><rect x="13.5" y="5" width="2" height="11" fill="#111"/></svg></div>
  <p class="t step" style="top:281px"><b>AS THE RETURN AND INVESTMENTS MULTIPLY<br>THE INTERESTS BEGINS TO COMPOUND ANNUALLY</b><br>The legal partner legally owns shares of stock within the<br>club and may redeem once a year or let money continue<br>to earn interest.</p>

  <div class="web-btn web-btn--dark">www.HARBORVALEVENTURES.com</div>
</section>

</body>
</html>
```